Graphics for Vorlani telehealth weight loss plans

Vorlani focuses on delivering medical weight-loss using prescription medicine and telehealth consults. Vorlani needs graphics for its ecommerce site for three weight loss plans. The plans are posted here with current graphics and descriptions of what is included with each plan. Please do not feel constrained by current graphics or styling.

- https://shop.vorlanicare.com/products/steady-horizon-plan
- https://shop.vorlanicare.com/products/amber-ridge-plan
- https://shop.vorlanicare.com/products/calm-harbor-plan

The graphics need to look good on mobile and desktop browsers.

```html
<!DOCTYPE html>
<html lang="en">
<head>
<meta charset="utf-8">
<title>Vorlani plan graphics</title>
<link rel="stylesheet" href="https://fonts.googleapis.com/css2?family=Barlow:wght@400;500;600;700&family=Source+Sans+3:wght@400&display=swap">
<style>
  :root {
    --board: #e2ebf5;
    --ink: #111418;
    --white: #ffffff;
    --navy: #04234a;
    --navy-deep: #021a3c;
    --teal: #0a6f73;
    --teal-bright: #20c9c6;
    --cyan: #17e3dc;
    --sky: #1bb2ee;
    --blue-top: #0b6aa8;
    --price-ink: #0a2f66;
    --frame-line: rgba(150, 200, 235, 0.55);
  }
  * { margin: 0; padding: 0; box-sizing: border-box; }
  html, body { width: 1200px; height: 640px; overflow: hidden; }
  body {
    background: var(--board);
    font-family: "Barlow", sans-serif;
    color: var(--white);
    position: relative;
  }
  .board-heading {
    position: absolute; top: 36px; left: 0; width: 1200px;
    text-align: center;
    font-family: "Source Sans 3", sans-serif;
    font-size: 30px; font-weight: 400; color: var(--ink);
    letter-spacing: -0.2px;
  }
  .plan-card {
    position: absolute; top: 122px; width: 339px; height: 479px;
    overflow: hidden;
    box-shadow: 0 6px 18px rgba(20, 40, 70, 0.25);
  }
  .plan-card > * { position: absolute; }
  .card-steady { left: 83px; background: linear-gradient(180deg, var(--navy-deep) 0%, #053a5a 45%, #0a6a6e 100%); }
  .card-calm { left: 431px; background: linear-gradient(180deg, var(--blue-top) 0%, #07477f 50%, var(--navy-deep) 100%); }
  .card-amber { left: 778px; background: linear-gradient(180deg, var(--navy-deep) 0%, #063f62 50%, #0a6f76 100%); }

  .brand-mark {
    display: flex; align-items: center; gap: 4px;
    font-weight: 500; font-size: 13px; letter-spacing: 0.5px; color: var(--white);
  }
  .brand-mark .brand-square { width: 9px; height: 9px; border: 1.5px solid var(--white); }

  .photo-slot { display: block; }

  .plan-title {
    font-weight: 700; line-height: 1.0; letter-spacing: 0.2px;
  }
  .price-tag {
    display: flex; align-items: center; justify-content: center;
    background: var(--white); color: var(--price-ink);
    font-weight: 700; font-size: 16px; border-radius: 2px;
  }
  .includes-heading { font-weight: 600; font-size: 16px; }
  .feature-list { list-style: none; }
  .feature-list li { font-size: 11px; font-weight: 400; line-height: 1.1; }

  /* Steady Horizon card */
  .card-steady .photo-slot {
    left: 225px; top: 0; width: 114px; height: 479px;
    background: linear-gradient(180deg, rgba(30,60,90,0.0) 0%, rgba(40,90,110,0.35) 40%, rgba(20,100,100,0.25) 100%);
  }
  .card-steady .brand-mark { left: 136px; top: 40px; }
  .card-steady .plan-title {
    left: 0; width: 339px; top: 97px; text-align: center;
    font-size: 26px; color: var(--teal-bright);
  }
  .card-steady .price-tag { left: 130px; top: 153px; width: 79px; height: 31px; }
  .card-steady .includes-heading { left: 21px; top: 203px; }
  .card-steady .feature-list { left: 21px; top: 240px; }
  .card-steady .feature-list li { height: 23.8px; font-size: 11.2px; }

  /* Calm Harbor card */
  .card-calm .brand-mark { left: 16px; top: 22px; }
  .card-calm .frame-lines { left: 0; top: 0; }
  .card-calm .photo-main { left: 107px; top: 41px; width: 124px; height: 169px; background: linear-gradient(160deg, #e9eef4, #b9c6d8); }
  .card-calm .photo-salad { left: 56px; top: 58px; width: 46px; height: 64px; background: linear-gradient(160deg, #4b5b62, #5f8a46); }
  .card-calm .photo-doctor { left: 26px; top: 126px; width: 76px; height: 64px; background: linear-gradient(160deg, #f0f0f0, #c9cfd5); }
  .card-calm .photo-meal { left: 236px; top: 58px; width: 76px; height: 64px; background: linear-gradient(160deg, #2b3038, #7a8a5a); }
  .card-calm .photo-measure { left: 236px; top: 126px; width: 46px; height: 64px; background: linear-gradient(160deg, #f1b7b0, #d98f8a); }
  .card-calm .plan-title {
    left: 0; width: 339px; top: 230px; text-align: center;
    font-size: 26px; color: var(--sky);
  }
  .card-calm .includes-heading {
    left: 115px; top: 270px; width: 108px; height: 24px;
    border: 1px solid rgba(255,255,255,0.7);
    display: flex; align-items: center; justify-content: center; font-size: 14px;
  }
  .card-calm .feature-list { left: 0; top: 309px; width: 339px; text-align: center; }
  .card-calm .feature-list li { height: 19.8px; }
  .card-calm .price-tag { left: 132px; top: 422px; width: 74px; height: 29px; font-size: 15px; }

  /* Amber Ridge card */
  .card-amber .brand-mark { left: 26px; top: 62px; }
  .card-amber .photo-meal { left: 213px; top: 55px; width: 126px; height: 100px; background: linear-gradient(160deg, #3a3f45, #6f8f3e 55%, #c9cfd2); }
  .card-amber .photo-scale { left: 213px; top: 159px; width: 126px; height: 272px; background: linear-gradient(180deg, #f2f2f0, #d8dcd8 60%, #b9bfbd); }
  .card-amber .plan-title { left: 26px; top: 106px; font-size: 24px; color: var(--cyan); }
  .card-amber .includes-heading {
    left: 26px; top: 189px; font-size: 15px;
    padding-bottom: 2px; border-bottom: 1px solid rgba(255,255,255,0.8);
  }
  .card-amber .feature-list { left: 26px; top: 225px; width: 185px; }
  .card-amber .feature-list li { font-size: 10.5px; margin-bottom: 7.4px; line-height: 1.08; }
  .card-amber .feature-list .highlight { color: var(--cyan); font-weight: 700; }
  .card-amber .price-tag {
    left: 27px; top: 402px; width: 74px; height: 29px;
    background: var(--cyan); color: var(--navy); font-size: 15px;
  }
</style>
</head>
<body>
  <h1 class="board-heading">Here are 3 templated for 3 plans. Thanks!</h1>

  <section class="plan-card card-steady">
    <div class="photo-slot" role="img" aria-label="Faded photo of a smiling woman in sportswear flexing her arm"></div>
    <div class="brand-mark"><span class="brand-square"></span>Vorlani</div>
    <h2 class="plan-title">Steady Horizon<br>Plan</h2>
    <div class="price-tag">$199.00</div>
    <h3 class="includes-heading">Plan includes</h3>
    <ol class="feature-list">
      <li>1. 100% online. No need to visit the office.</li>
      <li>2. Real Phentermine (37.5mg / pill) delivered to your door</li>
      <li>3. Phentermine prescription</li>
      <li>4. 1 month supply (30 pills)</li>
      <li>5. Medical consultation</li>
      <li>6. Expert nutrition consult</li>
      <li>7. Custom crafted diet plan to achieve your goals</li>
      <li>8. Nutrition coaching to improve your health and vitality</li>
      <li>9. Month-to-month pay as you go</li>
    </ol>
  </section>

  <section class="plan-card card-calm">
    <svg class="frame-lines" width="339" height="479" viewBox="0 0 339 479" aria-hidden="true">
      <g fill="none" stroke="var(--frame-line)" stroke-width="0.8">
        <rect x="36" y="84" width="70" height="140"/>
        <rect x="197" y="33" width="48" height="20"/>
        <rect x="250" y="154" width="72" height="70"/>
      </g>
    </svg>
    <div class="brand-mark"><span class="brand-square"></span>Vorlani</div>
    <div class="photo-slot photo-salad" role="img" aria-label="Photo of hands holding a bowl of fresh salad"></div>
    <div class="photo-slot photo-doctor" role="img" aria-label="Photo of a doctor in a white coat"></div>
    <div class="photo-slot photo-main" role="img" aria-label="Photo of a woman holding a green apple with a measuring tape at her waist"></div>
    <div class="photo-slot photo-meal" role="img" aria-label="Photo of a packed healthy meal box on a dark table"></div>
    <div class="photo-slot photo-measure" role="img" aria-label="Photo of a waist being measured with a tape"></div>
    <h2 class="plan-title">Calm Harbor Plan</h2>
    <h3 class="includes-heading">Plan includes</h3>
    <ul class="feature-list">
      <li>100% online. No need to visit the office.</li>
      <li>Expert nutrition consult</li>
      <li>Custom crafted diet plan to achieve your goals</li>
      <li>Nutrition coaching to improve your health and vitality</li>
      <li>Month-to-month pay as you go</li>
    </ul>
    <div class="price-tag">$99.00</div>
  </section>

  <section class="plan-card card-amber">
    <div class="brand-mark"><span class="brand-square"></span>Vorlani</div>
    <div class="photo-slot photo-meal" role="img" aria-label="Photo of a healthy meal container with vegetables"></div>
    <div class="photo-slot photo-scale" role="img" aria-label="Photo of a woman in workout clothes standing on a bathroom scale"></div>
    <h2 class="plan-title">Amber Ridge<br>Plan</h2>
    <h3 class="includes-heading">Plan includes</h3>
    <ul class="feature-list">
      <li>100% online. No need to visit the office</li>
      <li>Real Phentermine (37.5mg / pill)<br>delivered to your door</li>
      <li>Phentermine prescription</li>
      <li>1 month supply (30 pills)</li>
      <li>Medical consultation</li>
      <li><span class="highlight">FREE</span> Introductory Nutritionist<br>consult on your first month</li>
      <li>Month-to-month pay as you go</li>
    </ul>
    <div class="price-tag">$199.00</div>
  </section>
</body>
</html>
```